Corporate web site design for a blockchain oriented company

Design a web site for Tessaro. The company works on blockchain projects, mostly in B2B . Logo and content of the web site are attached with the project.

Corporate web sites means that we need to present the company and, at least, two of its projects.

Target Market(s)

B2B (Telecom, Gvt, online e-commerce web sites, banks, insurance ...)

Number of Pages Required

3 page

Font styles to use
Sans Serif

Requirements
Must have
• Landing page
• Page for KYC product
• Page for Loyalty product
• Team presentation
• Contact form
• Company presentation
• Several section can be in one page.
Nice to have
• Teaser video per project.
Should not have
• Heavy web site with a lot of animations.

```html
<!DOCTYPE html>
<html lang="en">
<head>
<meta charset="utf-8">
<title>Tessaro — Blockchain Solutions</title>
<link href="https://fonts.googleapis.com/css2?family=Michroma&family=Montserrat:wght@400;500;600&display=swap" rel="stylesheet">
<style>
:root{
  --ink:#1b1b1b;
  --text:#333333;
  --muted:#9a9a9a;
  --white:#ffffff;
  --paper:#f5f5f5;
  --field:#f1f1f1;
  --night:#0b1826;
  --night-deep:#050b12;
  --teal:#1f6f73;
}
*{margin:0;padding:0;box-sizing:border-box}
html,body{width:1200px;height:4390px;overflow:hidden}
body{font-family:"Montserrat",sans-serif;color:var(--text);background:var(--white);position:relative}
section,header,footer{position:absolute;left:0;width:1200px}

/* hero */
.hero{top:0;height:673px;background:radial-gradient(ellipse 55% 60% at 50% 38%,#5a5a5a 0%,#2a2a2a 50%,#0c0c0c 100%)}
.brand{position:absolute;top:260px;left:0;width:1200px;display:flex;justify-content:center;align-items:center;gap:26px}
.brand-dot{width:40px;height:40px;border-radius:50%;background:var(--white)}
.brand-name{font-weight:500;font-size:86px;letter-spacing:14px;color:var(--white)}
.main-nav{position:absolute;top:554px;left:0;width:1200px;display:flex;justify-content:center;gap:40px;font-family:"Michroma",sans-serif;font-size:14px;letter-spacing:1px;white-space:nowrap}
.main-nav a{color:#a8a8a8;text-decoration:none}
.main-nav a.current{color:var(--white)}

.section-title{position:absolute;left:0;width:1200px;display:flex;justify-content:center;align-items:center;gap:18px;font-family:"Michroma",sans-serif;font-weight:400;font-size:30px;color:var(--ink);letter-spacing:1px;white-space:nowrap}
.section-title .mark{width:34px;height:34px;border:3px solid var(--ink);border-radius:50%}
.section-title .light{color:var(--muted)}

.btn{position:absolute;display:flex;align-items:center;justify-content:center;border-radius:30px;background:linear-gradient(#3a3a3a,#050505);border:3px solid #bdbdbd;box-shadow:0 4px 8px rgba(0,0,0,.35);color:var(--white);font-family:"Michroma",sans-serif;font-size:15px;letter-spacing:1px;white-space:nowrap}

/* about */
.about{top:673px;height:542px}
.about .section-title{top:95px}
.about-copy{position:absolute;left:97px;top:190px;width:540px;font-size:18.5px;line-height:27px;color:var(--ink)}
.about .btn{left:97px;top:395px;width:212px;height:52px}
.about-video{position:absolute;left:688px;top:190px;width:417px;height:250px;background:radial-gradient(circle at 45% 60%,#8fd3ff 0%,#2c78c4 35%,#0b2c63 75%,#061634 100%);box-shadow:0 3px 10px rgba(0,0,0,.3);display:flex;align-items:center;justify-content:center}
.play{width:76px;height:76px;border-radius:50%;background:rgba(255,255,255,.75);display:flex;align-items:center;justify-content:center}

/* pillars */
.pillars{top:1215px;height:565px;background:var(--paper)}
.pillars-ring{position:absolute;left:380px;top:80px;width:440px;height:440px;border:28px solid #e9e9e9;border-radius:50%}
.pillars-brand{position:absolute;left:0;top:270px;width:1200px;display:flex;justify-content:center;align-items:center;gap:14px}
.pillars-brand .dot{width:22px;height:22px;border-radius:50%;background:var(--ink)}
.pillars-brand span{font-weight:600;font-size:38px;letter-spacing:6px;color:var(--ink)}
.pillar{position:absolute;display:flex;gap:16px;align-items:flex-start;font-size:19px;line-height:26px;color:var(--text)}
.pillar svg{flex:none}
.pillar-team{left:340px;top:96px;width:520px}
.pillar-collab{left:122px;top:342px;width:400px}
.pillar-tech{left:726px;top:342px;width:400px}

/* products */
.products{top:1780px;height:907px;background:radial-gradient(ellipse 60% 50% at 8% 85%,rgba(31,111,115,.7) 0%,rgba(11,24,38,0) 70%),linear-gradient(160deg,#132636 0%,var(--night) 45%,var(--night-deep) 100%)}
.tabs{position:absolute;left:94px;top:93px;width:1012px;height:103px;display:flex}
.tab{flex:1;display:flex;align-items:center;justify-content:center;gap:16px;font-family:"Michroma",sans-serif;font-size:26px;color:var(--white);letter-spacing:1px;white-space:nowrap}
.tab.active{border:2px solid #d0d0d0;border-bottom:none}
.tab.idle{border:2px solid #d0d0d0}
.tab .ring{width:26px;height:26px;border:2px solid #d0d0d0;border-radius:50%}
.products h3{position:absolute;top:246px;left:0;width:1200px;text-align:center;font-weight:500;font-size:24px;color:var(--white)}
.products .lead{position:absolute;top:318px;left:120px;width:960px;text-align:center;font-size:19px;line-height:31px;color:var(--white)}
.benefit{position:absolute;display:flex;gap:18px;width:330px;color:#c9d2d9;font-size:19px;line-height:25px}
.benefit svg{flex:none}
.benefit strong{display:block;font-weight:500;color:var(--white)}
.products .btn{left:492px;top:755px;width:216px;height:58px}

/* news */
.news{top:2687px;height:709px}
.news .section-title{top:100px}
.news-card{position:absolute;top:182px;width:320px;height:440px;background:var(--white);box-shadow:0 2px 12px rgba(0,0,0,.18)}
.news-card .thumb{position:absolute;left:22px;top:23px;width:276px;height:181px}
.news-date{position:absolute;top:236px;left:0;width:100%;display:flex;justify-content:center;align-items:center;gap:12px;font-size:16px;color:var(--text)}
.news-card h4{position:absolute;left:22px;top:282px;font-weight:500;font-size:21px;color:var(--ink);white-space:nowrap}
.news-card p{position:absolute;left:22px;top:318px;width:280px;font-size:17px;line-height:24px;color:var(--text)}

/* contact */
.contact{top:3396px;height:526px}
.contact .section-title{top:90px}
.field{position:absolute;background:var(--field);font-size:14px;color:var(--ink);padding:12px 14px}
.contact .btn{left:512px;top:389px;width:180px;height:46px;font-family:"Montserrat",sans-serif;font-size:16px;border-width:2px}

/* footer */
.site-footer{top:3922px;height:468px;background:radial-gradient(ellipse 45% 70% at 50% 40%,#15324a 0%,#08121d 60%,#03070c 100%);color:var(--white)}
.footer-brand{position:absolute;top:55px;left:0;width:1200px;display:flex;justify-content:center;align-items:center;gap:14px}
.footer-brand span{font-weight:500;font-size:48px;letter-spacing:8px}
.footer-brand .dot{width:20px;height:20px;border-radius:50%;background:var(--white)}
.footer-col{position:absolute;top:160px;font-size:13px;line-height:20px;white-space:nowrap}
.footer-col h5{font-weight:600;font-size:14px;letter-spacing:1px;padding-bottom:8px;margin-bottom:18px;border-bottom:1px solid #3c4c5c;display:inline-block;min-width:100px}
.contact-line{display:flex;gap:10px;align-items:flex-start;margin-bottom:14px}
.contact-line svg{flex:none}
.social{display:flex;align-items:center;gap:12px;margin-bottom:16px}
.social i{width:18px;height:18px;border-radius:50%;background:#2e8fd8;display:block}
.newsletter{display:flex}
.newsletter .email{width:160px;height:36px;background:var(--white);color:var(--ink);font-size:12px;padding:10px}
.newsletter .signup{width:96px;height:36px;background:#0b0b0b;border:1px solid #555;font-weight:600;font-size:13px;display:flex;align-items:center;justify-content:center}
.copyright{position:absolute;top:425px;left:0;width:1200px;text-align:center;font-size:11px;color:#a4a4a4;letter-spacing:1px}
</style>
</head>
<body>

<header class="hero">
  <div class="brand"><span class="brand-dot"></span><span class="brand-name">TESSARO</span></div>
  <nav class="main-nav">
    <a class="current" href="#">HOME</a><a href="#">ABOUT</a><a href="#">WHY TESSARO</a><a href="#">LOYALINK</a><a href="#">VERIDEX</a><a href="#">NEWS</a><a href="#">CONTACT</a>
  </nav>
</header>

<section class="about">
  <h2 class="section-title"><span class="mark"></span>ABOUT TESSARO</h2>
  <p class="about-copy">Lorem ipsum dolor sit amet, consectetur adipiscing elit, sed do eiusmod tempor incididunt ut labore et dolore magna aliqua. Ut enim ad minim veniam, qi nostrud exercitation ullamco laboris nisi ut aliquip ex ea commodo consequat. Duis aute irure dolor in reprehenderit in voluptate velit esse.</p>
  <div class="btn">LEARN MORE</div>
  <div class="about-video" role="img" aria-label="Company teaser video: glowing network over the globe">
    <div class="play"><svg width="30" height="34" viewBox="0 0 30 34"><path d="M4 2 L28 17 L4 32 Z" fill="#2c78c4"/></svg></div>
  </div>
</section>

<section class="pillars">
  <div class="pillars-ring"></div>
  <div class="pillars-brand"><span class="dot"></span><span>TESSARO</span></div>
  <div class="pillar pillar-team">
    <svg width="64" height="44" viewBox="0 0 64 44" fill="none" stroke="#444" stroke-width="2.5"><circle cx="32" cy="12" r="7"/><circle cx="14" cy="16" r="6"/><circle cx="50" cy="16" r="6"/><path d="M20 40 v-8 a12 10 0 0 1 24 0 v8 z"/><path d="M4 40 v-6 a10 8 0 0 1 14 -6"/><path d="M60 40 v-6 a10 8 0 0 0 -14 -6"/></svg>
    <p>The company is lead by a team with tremendous expertise in the field of blockchain, mobile, IT, payment and financial sector.</p>
  </div>
  <div class="pillar pillar-collab">
    <svg width="56" height="56" viewBox="0 0 56 56" fill="none" stroke="#444" stroke-width="2.5"><path d="M28 4 L49 16 V40 L28 52 L7 40 V16 Z"/><circle cx="28" cy="28" r="6"/><circle cx="28" cy="4" r="3"/><circle cx="49" cy="16" r="3"/><circle cx="49" cy="40" r="3"/><circle cx="28" cy="52" r="3"/><circle cx="7" cy="40" r="3"/><circle cx="7" cy="16" r="3"/><path d="M28 7 V22 M46 18 L33 25 M46 38 L33 31 M28 49 V34 M10 38 L23 31 M10 18 L23 25"/></svg>
    <p>Tessaro solves business problems using blockchain technology and create a collaborative environment for organisation</p>
  </div>
  <div class="pillar pillar-tech">
    <p>Tessaro technology leverages on the most advanced blockchain technology that might not be available a few years ago</p>
    <svg width="56" height="56" viewBox="0 0 56 56" fill="none" stroke="#444" stroke-width="2.5"><rect x="20" y="20" width="16" height="16"/><rect x="22" y="2" width="12" height="10"/><rect x="22" y="44" width="12" height="10"/><rect x="2" y="23" width="10" height="10"/><rect x="44" y="23" width="10" height="10"/><path d="M28 12 V20 M28 36 V44 M12 28 H20 M36 28 H44"/></svg>
  </div>
</section>

<section class="products">
  <div class="tabs">
    <div class="tab active"><span class="ring"></span>LOYALINK</div>
    <div class="tab idle"><span class="ring"></span>VERIDEX</div>
  </div>
  <h3>Intuitive partnership solution</h3>
  <p class="lead">Tessaro connects partners via Loyalink to provide your loyalty points with more capabilities and brings unlimited cross-sector potential to your customers.</p>

  <div class="benefit" style="left:94px;top:440px">
    <svg width="60" height="40" viewBox="0 0 60 40" fill="none" stroke="#fff" stroke-width="3"><path d="M30 20 C22 8 6 8 6 20 C6 32 22 32 30 20 C38 8 54 8 54 20 C54 32 38 32 30 20 Z"/></svg>
    <div><strong>Limitless</strong>Not affected by the amount of partners on the network</div>
  </div>
  <div class="benefit" style="left:462px;top:440px">
    <svg width="60" height="56" viewBox="0 0 60 56" fill="none" stroke="#fff" stroke-width="3.5"><path d="M8 46 A24 24 0 1 1 52 46"/><path d="M30 34 L42 18"/><circle cx="30" cy="34" r="4" fill="#fff"/></svg>
    <div><strong>Speed</strong>Real-time settlement</div>
  </div>
  <div class="benefit" style="left:830px;top:440px">
    <svg width="60" height="56" viewBox="0 0 60 56" fill="#fff"><path d="M30 4 L56 17 L30 30 L4 17 Z"/><path d="M4 27 L30 40 L56 27 L56 32 L30 45 L4 32 Z"/><path d="M4 37 L30 50 L56 37 L56 42 L30 55 L4 42 Z" opacity=".8"/></svg>
    <div><strong>Transparent</strong>Transactions can be viewed by anyone</div>
  </div>
  <div class="benefit" style="left:94px;top:585px">
    <svg width="60" height="56" viewBox="0 0 60 56" fill="none" stroke="#fff" stroke-width="4"><path d="M40 14 C36 8 20 8 20 18 C20 28 42 26 42 38 C42 48 24 48 19 42"/><path d="M30 2 V54"/></svg>
    <div><strong>Cost</strong>Eliminating manual efforts required for business partnerships</div>
  </div>
  <div class="benefit" style="left:462px;top:585px">
    <svg width="60" height="60" viewBox="0 0 60 60" fill="none" stroke="#fff" stroke-width="3.5"><path d="M52 30 A22 22 0 1 1 44 13"/><path d="M38 8 L46 12 L42 20"/><text x="30" y="37" font-family="Montserrat,sans-serif" font-size="18" font-weight="600" fill="#fff" stroke="none" text-anchor="middle">24</text></svg>
    <div><strong>Access</strong>Available 24/7</div>
  </div>
  <div class="btn">LEARN MORE</div>
</section>

<section class="news">
  <h2 class="section-title"><span class="mark"></span><span class="light">LATEST</span> NEWS</h2>

  <article class="news-card" style="left:94px">
    <div class="thumb" role="img" aria-label="Photo of people working with laptops and charts" style="background:linear-gradient(135deg,#f4f4f4 0%,#cfd3d8 50%,#8d949c 100%)"></div>
    <div class="news-date"><svg width="20" height="20" viewBox="0 0 20 20" fill="none" stroke="#555" stroke-width="1.8"><rect x="2" y="4" width="16" height="14"/><path d="M2 8 H18 M6 2 V6 M14 2 V6"/></svg>Jan 4, 2019</div>
    <h4>Solving Problems</h4>
    <p>Consectetur adipiscing elit, se do eiusmod tempor incididun ut labore et dolore magna aliq ua ut enim ad minim veniam.</p>
  </article>

  <article class="news-card" style="left:439px">
    <div class="thumb" role="img" aria-label="Photo of business partners shaking hands in an office" style="background:linear-gradient(135deg,#7c8894 0%,#3d4954 50%,#1e252c 100%)"></div>
    <div class="news-date"><svg width="20" height="20" viewBox="0 0 20 20" fill="none" stroke="#555" stroke-width="1.8"><rect x="2" y="4" width="16" height="14"/><path d="M2 8 H18 M6 2 V6 M14 2 V6"/></svg>Jan 3, 2019</div>
    <h4>Veridex Technology</h4>
    <p>Consectetur adipiscing elit, se do eiusmod tempor incididun ut labore et dolore magna aliq ua ut enim ad minim veniam.</p>
  </article>

  <article class="news-card" style="left:784px">
    <div class="thumb" role="img" aria-label="Abstract purple particle wave on black" style="background:radial-gradient(ellipse at 55% 45%,#b66be0 0%,#5b2a8a 40%,#140a22 85%)"></div>
    <div class="news-date"><svg width="20" height="20" viewBox="0 0 20 20" fill="none" stroke="#555" stroke-width="1.8"><rect x="2" y="4" width="16" height="14"/><path d="M2 8 H18 M6 2 V6 M14 2 V6"/></svg>Dec 30, 2018</div>
    <h4>Blockchain Technology</h4>
    <p>Consectetur adipiscing elit, se do eiusmod tempor incididun ut labore et dolore magna aliq ua ut enim ad minim veniam.</p>
  </article>
</section>

<section class="contact">
  <h2 class="section-title"><span class="mark"></span><span class="light">CONTACT</span> US</h2>
  <div class="field" style="left:117px;top:178px;width:313px;height:47px">Your Name</div>
  <div class="field" style="left:445px;top:178px;width:313px;height:47px">Your Email</div>
  <div class="field" style="left:776px;top:178px;width:310px;height:47px">Your Subject</div>
  <div class="field" style="left:117px;top:237px;width:969px;height:134px">Message</div>
  <div class="btn">Submit</div>
</section>

<footer class="site-footer">
  <div class="footer-brand"><span class="dot"></span><span>TESSARO</span></div>

  <div class="footer-col" style="left:126px">
    <h5>QUICK LINKS</h5><br>
    Home<br>About<br>Why Tessaro<br>Loyalink<br>Veridex<br>News<br>Contact
  </div>
  <div class="footer-col" style="left:293px">
    <h5>COMPANY</h5><br>
    Our Team<br>Mission<br>Vision
  </div>
  <div class="footer-col" style="left:439px">
    <h5>CONTACT</h5>
    <div class="contact-line"><svg width="18" height="18" viewBox="0 0 18 18" fill="none" stroke="#fff" stroke-width="1.5"><circle cx="9" cy="9" r="8"/><path d="M9 4 C6.5 4 5.5 6 5.5 7.5 C5.5 10 9 14 9 14 C9 14 12.5 10 12.5 7.5 C12.5 6 11.5 4 9 4 Z"/></svg><span>Tessaro<br>48 Harbour Line<br>Marina Quay</span></div>
    <div class="contact-line"><svg width="18" height="18" viewBox="0 0 18 18" fill="none" stroke="#fff" stroke-width="1.5"><circle cx="9" cy="9" r="8"/><path d="M6 5 L8 5 L8.5 7.5 L7.5 8.5 C8 10 9 11 10.5 11.5 L11.5 10.5 L14 11 L13 13 C9 13 5 9 6 5 Z"/></svg><span>1800 555 0142</span></div>
    <div class="contact-line"><svg width="18" height="18" viewBox="0 0 18 18" fill="none" stroke="#fff" stroke-width="1.5"><circle cx="9" cy="9" r="8"/><rect x="5" y="6" width="8" height="6"/><path d="M5 6 L9 9.5 L13 6"/></svg><span>hello@tessaro-chain.com</span></div>
  </div>
  <div class="footer-col" style="left:664px">
    <h5>FOLLOW US</h5>
    <div class="social"><i></i>Friendbook</div>
    <div class="social"><i></i>Linkwork</div>
    <div class="social"><i></i>Chirper</div>
  </div>
  <div class="footer-col" style="left:822px">
    <h5>NEWSLETTER</h5>
    <div class="newsletter"><div class="email">Enter Email Address</div><div class="signup">SIGN UP</div></div>
  </div>

  <p class="copyright">COPYRIGHT © 2019 TESSARO. ALL RIGHTS RESERVED.</p>
</footer>

</body>
</html>
```